Business card design needed

Our modern electrical contracting company requires business card design utilising our logo and incorporating our tag line "Service when you need it". We specialise in assisting our customers 24/7 offering a breakdown service.

Industry/Entity Type

Electrical

Contact Information for Business Card

Marcus Penhale, Electrical contractor,Tel: (08) 8456 3071, Fax: (08) 8679 4315, Mob 0438 562 740, Email: marcus.penhale@brightwirepower.com.au, Web: www.brightwirepower.com.au

Requirements
Must have
• we require a 2 sided card.
Front- Logo, tag line and contact information.
Rear- service when you need it! Call now for our 24/7 breakdown service

```html
<!DOCTYPE html>
<html lang="en">
<head>
<meta charset="utf-8">
<title>Brightwire Power – Business Card</title>
<link href="https://fonts.googleapis.com/css2?family=Arimo:wght@400;700&family=Roboto+Condensed:wght@400&display=swap" rel="stylesheet">
<style>
  :root {
    --card-bg: #ffffff;
    --brand-blue: #1f86ea;
    --band-blue: #1a7ff0;
    --ink: #111111;
    --on-blue: #ffffff;
  }
  html, body {
    margin: 0;
    padding: 0;
    overflow: hidden;
    background: var(--card-bg);
  }
  .card {
    position: relative;
    width: 1200px;
    height: 676px;
    background: var(--card-bg);
    overflow: hidden;
    font-family: "Roboto Condensed", "Arial Narrow", sans-serif;
    color: var(--ink);
  }
  .brand-mark {
    position: absolute;
    left: 245px;
    top: 74px;
    width: 132px;
    height: 132px;
    border-radius: 50%;
    background: var(--brand-blue);
  }
  .brand-name {
    position: absolute;
    left: 64px;
    top: 222px;
    width: 496px;
    margin: 0;
    font-family: "Arimo", Arial, sans-serif;
    font-weight: 700;
    font-size: 45px;
    line-height: 1;
    letter-spacing: 0.5px;
    color: var(--brand-blue);
    text-align: center;
    white-space: nowrap;
  }
  .tagline {
    position: absolute;
    left: 259px;
    top: 276px;
    margin: 0;
    font-size: 29px;
    line-height: 1;
    white-space: nowrap;
  }
  .contact-person {
    position: absolute;
    right: 52px;
    top: 378px;
    text-align: right;
    white-space: nowrap;
  }
  .person-name {
    margin: 0;
    font-family: "Arimo", Arial, sans-serif;
    font-weight: 700;
    font-size: 36px;
    line-height: 42px;
  }
  .person-role {
    margin: 0;
    font-size: 30px;
    line-height: 36px;
  }
  .person-mobile,
  .person-email {
    margin: 0;
    font-size: 29px;
    line-height: 31px;
  }
  .person-mobile { margin-top: 10px; }
  .office-lines {
    position: absolute;
    left: 375px;
    top: 548px;
    font-size: 30px;
    line-height: 1;
    white-space: nowrap;
  }
  .office-line { margin: 0; }
  .office-line .label {
    display: inline-block;
    width: 66px;
  }
  .office-line + .office-line { margin-top: 11px; }
  .rule {
    position: absolute;
    left: 373px;
    top: 586px;
    width: 827px;
    height: 2px;
    background: var(--band-blue);
  }
  .web-band {
    position: absolute;
    left: 0;
    top: 0;
    width: 1200px;
    height: 676px;
  }
  .web-address {
    position: absolute;
    left: 691px;
    top: 595px;
    margin: 0;
    font-size: 30px;
    line-height: 1;
    color: var(--on-blue);
    white-space: nowrap;
  }
</style>
</head>
<body>
  <div class="card">
    <div class="brand-mark" aria-hidden="true"></div>
    <h1 class="brand-name">BRIGHTWIRE POWER</h1>
    <p class="tagline">...Service when you need it</p>

    <div class="contact-person">
      <p class="person-name">Marcus Penhale</p>
      <p class="person-role">Electrical contractor</p>
      <p class="person-mobile">0438 562 740</p>
      <p class="person-email">marcus.penhale@brightwirepower.com.au</p>
    </div>

    <div class="rule"></div>
    <svg class="web-band" viewBox="0 0 1200 676" aria-hidden="true">
      <polygon points="674,587 1200,587 1200,676 696,676" fill="var(--band-blue)"/>
    </svg>

    <div class="office-lines">
      <p class="office-line"><span class="label">Tel</span>: (08) 8456 3071</p>
      <p class="office-line"><span class="label">Fax</span>: (08) 8679 4315</p>
    </div>

    <p class="web-address">Web: www.brightwirepower.com.au</p>
  </div>
</body>
</html>
```